Create Flyer for RGB wall washers

We are launching a product that is run by an app and allows you to customize your exterior lighting at the touch of a button. We want to create the image of being technologically advanced company who is easy to work with. Looking for streamlined design which will reflect how we operate as a company. We will be printing at pressmarlow.com so please have the correct format. I am looking for this to be single sided thank you for your time and submission

Target Market(s)

Residential and commercial

Industry/Entity Type

Product

Requirements
Must have
• clean layout
• easy to read
• Common fonts
• Color scheme must work with logo (we can provide a black background to logo in needed)
Nice to have
• Nicely displayed images to help sell the idea
Should not have
• Too busy background

```html
<!DOCTYPE html>
<html lang="en">
<head>
<meta charset="utf-8">
<title>Outdoor Lighting Flyer</title>
<link rel="stylesheet" href="https://fonts.googleapis.com/css2?family=Exo+2:wght@800;900&family=Ubuntu:wght@400;500&family=Roboto+Condensed:wght@400;700&display=swap">
<style>
  :root {
    --page-bg: #e9e6e1;
    --sheet-top: #f7f8fa;
    --sheet-bottom: #e4e7ec;
    --brand-light: #3aaae8;
    --brand-mid: #2384d2;
    --brand-deep: #1a5fb0;
    --caption-light: #2b9ad8;
    --caption-mid: #1d7fc4;
    --caption-dark: #2b4f86;
    --body-text: #555a60;
    --heading-blue: #1f4f93;
    --white: #ffffff;
    --silver: #e3e6ea;
  }
  * { box-sizing: border-box; margin: 0; padding: 0; }
  html, body { width: 1200px; height: 902px; overflow: hidden; }
  body { background: var(--page-bg); position: relative; font-family: "Ubuntu", sans-serif; }

  .flyer {
    position: absolute; left: 138px; top: 124px; width: 924px; height: 654px;
    background: linear-gradient(180deg, var(--sheet-top), var(--sheet-bottom));
    overflow: hidden;
  }
  .flyer__header {
    position: absolute; left: 0; top: 0; width: 924px; height: 132px;
    background: linear-gradient(180deg, var(--brand-light), var(--brand-deep));
    display: flex; align-items: center; justify-content: center; text-align: center;
  }
  .flyer__title {
    font-family: "Exo 2", sans-serif; font-weight: 900; font-size: 45px; line-height: 46px;
    letter-spacing: 1.5px; text-transform: uppercase;
    background: linear-gradient(180deg, var(--white) 40%, var(--silver) 60%, #b9c0c8);
    -webkit-background-clip: text; background-clip: text; color: transparent;
  }

  .scene { position: absolute; width: 273px; }
  .scene__caption {
    font-size: 14px; line-height: 18px; text-align: center; text-transform: uppercase;
    height: 36px;
  }
  .scene--everyday { left: 34px; top: 148px; }
  .scene--events { left: 325px; top: 148px; }
  .scene--holiday { left: 615px; top: 148px; }
  .scene--everyday .scene__caption { color: var(--caption-light); }
  .scene--events .scene__caption { color: var(--caption-mid); font-weight: 500; }
  .scene--holiday .scene__caption { color: var(--caption-dark); }
  .scene__photo { display: block; width: 273px; height: 204px; }
  .scene--holiday .scene__photo { margin-top: 2px; }
  .photo--white { background: linear-gradient(180deg, #1b2434 0%, #6c5d70 45%, #2b2320 100%); }
  .photo--color { background: linear-gradient(90deg, #4a2d7a 0%, #6a3fb0 35%, #3852b8 60%, #b8342a 85%, #3a2418 100%); }
  .photo--holiday { background: linear-gradient(90deg, #1e4a30 0%, #3c8a4a 35%, #8a3a2c 65%, #b83040 90%, #2a1c18 100%); }

  .app-screens {
    position: absolute; left: 34px; top: 401px; width: 176px; height: 86px;
    background: linear-gradient(90deg, #d6d9de, #f2f3f5 50%, #cfd3d8);
  }
  .app-banner {
    position: absolute; left: 212px; top: 406px; width: 676px; height: 77px;
    background: linear-gradient(180deg, var(--brand-light), var(--brand-deep));
    display: flex; align-items: center; padding-left: 14px;
  }
  .app-banner__text {
    font-family: "Exo 2", sans-serif; font-weight: 800; font-size: 18.5px; line-height: 23px;
    letter-spacing: 0.6px; color: var(--white); text-transform: uppercase;
  }

  .details { position: absolute; left: 34px; top: 495px; width: 454px; }
  .details__copy {
    font-size: 14px; line-height: 19px; color: var(--body-text); text-align: justify;
  }
  .details__price {
    margin-top: 14px; font-family: "Roboto Condensed", sans-serif; font-weight: 700;
    font-size: 18px; line-height: 20px; color: var(--heading-blue); text-transform: uppercase;
  }
  .details__note { font-size: 13px; line-height: 15px; color: var(--body-text); }
  .details__contact {
    margin-top: 6px; font-family: "Roboto Condensed", sans-serif; font-weight: 700;
    font-size: 17.5px; color: var(--heading-blue); word-spacing: 2px;
  }
  .details__contact span { margin-left: 14px; }

  .brand-box {
    position: absolute; left: 518px; top: 538px; width: 370px; height: 93px;
    background: var(--white); display: flex; align-items: center; justify-content: center; gap: 14px;
  }
  .brand-box__mark { width: 26px; height: 26px; background: var(--brand-mid); }
  .brand-box__name {
    font-family: "Exo 2", sans-serif; font-weight: 800; font-size: 30px;
    letter-spacing: 1px; color: var(--brand-mid); text-transform: uppercase;
  }

  .flyer__footer-bar {
    position: absolute; left: 30px; top: 644px; width: 858px; height: 10px; background: var(--brand-light);
  }
</style>
</head>
<body>
  <main class="flyer">
    <header class="flyer__header">
      <h1 class="flyer__title">Control your outdoor lighting<br>with the touch of a button</h1>
    </header>

    <section class="scene scene--everyday">
      <p class="scene__caption">Standard lighting for everyday use</p>
      <div class="scene__photo photo--white" role="img" aria-label="House at night lit with white wall-wash and tree up-lights"></div>
    </section>
    <section class="scene scene--events">
      <p class="scene__caption">Special events you choose the colors and effects</p>
      <div class="scene__photo photo--color" role="img" aria-label="House at night washed in purple, blue and red light"></div>
    </section>
    <section class="scene scene--holiday">
      <p class="scene__caption" style="padding-top:2px">Holiday lighting made simple</p>
      <div class="scene__photo photo--holiday" role="img" aria-label="House at night lit in holiday green and red"></div>
    </section>

    <div class="app-screens" role="img" aria-label="Row of phones showing the lighting control app screens"></div>
    <div class="app-banner">
      <p class="app-banner__text">Change the color or effect with the touch of a finger<br>through an easy to use app from your phone or tablet</p>
    </div>

    <section class="details">
      <p class="details__copy">State-of-the-Art lighting system that will wash your exterior walls with light or landscape plantings with up-lights. Its year-round lighting at a fraction of the cost.</p>
      <p class="details__price">Prices' starting at $799 including installation</p>
      <p class="details__note">- this system is scalable.</p>
      <p class="details__contact">Call us today 404 555 0172<span>www.brightfield-lighting.com</span></p>
    </section>

    <div class="brand-box">
      <span class="brand-box__mark"></span>
      <span class="brand-box__name">Brightfield Lighting</span>
    </div>

    <div class="flyer__footer-bar"></div>
  </main>
</body>
</html>
```